Business Card and Stationary design for new logo
Bright Harbour Makeovers
Professional
Tessa Whitlock & Lewis Whitlock
Director
42 Quenby Crescent
Baulkham Hills NSW 2153
brightharbourmakeovers@fernpost.example
ABN:284 907 362
Color combinations need to remain within company palette of ORANGE, TAN, BLACK AND WHITE. Would prefer ORANGE as main background color for business card design and therefore will need to invert actual logo colors to be able to see all of the design. Would prefer BLACK as the main background color for stationary design as currently have templates where the logo would need to be inserted however would be interested in seeing other designs to make final decision.

```html
<!DOCTYPE html>
<html lang="en">
<head>
<meta charset="utf-8">
<title>Bright Harbour Makeovers Stationery</title>
<link href="https://fonts.googleapis.com/css2?family=Open+Sans:wght@400;600;700&display=swap" rel="stylesheet">
<style>
:root{
  --bg:#9c9d9f;
  --paper:#ffffff;
  --ink:#1f1f1f;
  --black:#161616;
  --orange:#e8731a;
  --orange-light:#f39a3c;
  --tan:#d9c2a3;
  --grey:#8a8a8a;
  --faint:#ececec;
}
*{margin:0;padding:0;box-sizing:border-box}
html,body{width:1200px;height:876px;overflow:hidden}
body{background:var(--bg);font-family:"Open Sans",Arial,sans-serif;color:var(--ink);position:relative}
.item{position:absolute;background:var(--paper);box-shadow:0 3px 8px rgba(0,0,0,.35);overflow:hidden}
.brand{display:flex;align-items:center;gap:6px;font-weight:700;color:var(--ink);white-space:nowrap;line-height:1}
.brand .dot{border-radius:50%;background:var(--orange);flex:none}
.brand.light{color:#fff}
.small{font-size:5px;color:var(--grey);line-height:1.6}

/* envelopes */
.envelope-back{left:43px;top:29px;width:353px;height:140px}
.envelope-back .flap{position:absolute;inset:0}
.envelope-front{left:43px;top:149px;width:353px;height:187px}
.envelope-front .flap{position:absolute;left:0;top:0;width:100%;height:110px}
.envelope-front .seal{position:absolute;left:175px;top:84px;width:24px;height:24px}

/* business cards */
.card{width:274px;height:149px;top:38px}
.card-one{left:557px}
.card-two{left:902px}
.card .names{position:absolute;left:0;top:0;width:100%;height:26px;background:var(--black);color:#fff;font-size:8px;font-weight:600;padding:8px 0 0 74px}
.card .names span{font-weight:400;color:#bbb}
.card .brand{position:absolute;left:74px;top:40px;font-size:10px}
.card .brand .dot{width:16px;height:16px}
.card .details{position:absolute;left:74px;top:66px}
.card .band{position:absolute;left:0;bottom:0;width:100%;height:50px;background:linear-gradient(90deg,var(--orange-light),var(--orange))}
.card-back{left:902px;top:202px;width:274px;height:139px;border-radius:4px}
.card-back .brand{position:absolute;left:50%;top:50%;transform:translate(-50%,-50%);font-size:11px}
.card-back .brand .dot{width:18px;height:18px}

/* DL envelope */
.dl{left:480px;top:173px;width:348px;height:168px}
.dl .brand{position:absolute;left:16px;top:16px;font-size:10px}
.dl .brand .dot{width:16px;height:16px}
.dl .details{position:absolute;left:24px;top:40px}
.dl .band{position:absolute;left:0;bottom:0;width:100%;height:42px}

/* letterheads */
.sheet{top:389px;width:358px;height:458px}
.sheet-one{left:72px}
.sheet-two{left:466px}
.sheet-fax{left:832px;width:356px}
.sheet .top-rule{position:absolute;left:0;top:0;width:100%;height:7px;background:var(--black)}
.sheet .brand{position:absolute;left:36px;top:30px;font-size:12px}
.sheet .brand .dot{width:20px;height:20px}
.sheet .mark{position:absolute;left:80px;top:120px;width:200px;height:200px;border-radius:50%;background:radial-gradient(circle,#f6f6f6 0,#e6e6e6 70%,#f3f3f3 100%)}
.sheet .footer{position:absolute;left:0;bottom:0;width:100%;height:56px;background:linear-gradient(90deg,var(--orange-light),var(--orange));padding:14px 0 0 0;text-align:center}
.sheet .footer .small{color:#fff}
.fax-contact{position:absolute;right:20px;top:30px;text-align:right}
.fax-title{position:absolute;left:20px;top:112px;font-size:20px;font-weight:400;letter-spacing:1px}
.fax-table{position:absolute;left:20px;top:148px;width:316px;border-collapse:collapse;font-size:6px;color:#444}
.fax-table td{border-bottom:1px solid #bbb;height:17px;vertical-align:bottom;padding-bottom:2px}
.fax-table td.label{width:30px}
.fax-options{position:absolute;left:20px;top:236px;display:flex;gap:13px;font-size:5px;color:#444}
.fax-options span{display:flex;align-items:center;gap:3px}
.fax-options i{width:6px;height:6px;border:1px solid #777;display:inline-block}
</style>
</head>
<body>

<div class="item envelope-back">
  <svg class="flap" viewBox="0 0 353 140" preserveAspectRatio="none">
    <rect width="353" height="140" fill="#f4f4f4"/>
    <path d="M0 0 H353 V30 L176 80 L0 30 Z" fill="#161616"/>
  </svg>
</div>

<div class="item envelope-front">
  <svg class="flap" viewBox="0 0 353 110" preserveAspectRatio="none">
    <path d="M0 0 H353 L176 108 Z" fill="#e8731a"/>
    <path d="M0 0 H353 L176 94 Z" fill="#ffffff"/>
  </svg>
  <svg class="seal" viewBox="0 0 24 24"><circle cx="12" cy="12" r="11" fill="#e8731a"/></svg>
</div>

<div class="item card card-one">
  <div class="names">Tessa Whitlock &amp; Lewis Whitlock <span>| Director</span></div>
  <div class="brand"><span class="dot"></span>Bright Harbour Makeovers</div>
  <div class="details small">42 Quenby Crescent<br>brightharbourmakeovers@fernpost.example<br>ABN: 284 907 362</div>
  <div class="band"></div>
</div>

<div class="item card card-two">
  <div class="names">Tessa Whitlock &amp; Lewis Whitlock <span>| Director</span></div>
  <div class="brand"><span class="dot"></span>Bright Harbour Makeovers</div>
  <div class="details small">42 Quenby Crescent<br>brightharbourmakeovers@fernpost.example<br>ABN: 284 907 362</div>
  <div class="band"></div>
</div>

<div class="item dl">
  <div class="brand"><span class="dot"></span>Bright Harbour Makeovers</div>
  <div class="details small">42 Quenby Crescent</div>
  <svg class="band" viewBox="0 0 348 42" preserveAspectRatio="none">
    <path d="M0 14 Q174 0 348 10 V42 H0 Z" fill="#e8731a"/>
  </svg>
</div>

<div class="item card-back">
  <div class="brand"><span class="dot"></span>Bright Harbour Makeovers</div>
</div>

<div class="item sheet sheet-one">
  <div class="top-rule"></div>
  <div class="brand"><span class="dot"></span>Bright Harbour Makeovers</div>
  <div class="mark" role="img" aria-label="Large faint brand mark"></div>
  <div class="footer"><p class="small">42 Quenby Crescent<br>brightharbourmakeovers@fernpost.example<br>ABN: 284 907 362</p></div>
</div>

<div class="item sheet sheet-two">
  <div class="top-rule" style="background:var(--paper)"></div>
  <div class="brand"><span class="dot"></span>Bright Harbour Makeovers</div>
  <div class="mark" role="img" aria-label="Large faint brand mark"></div>
  <div class="footer"><p class="small">42 Quenby Crescent<br>brightharbourmakeovers@fernpost.example<br>ABN: 284 907 362</p></div>
</div>

<div class="item sheet sheet-fax">
  <div class="brand"><span class="dot"></span>Bright Harbour Makeovers</div>
  <div class="fax-contact small">42 Quenby Crescent<br>ABN: 284 907 362</div>
  <h1 class="fax-title">FAX</h1>
  <table class="fax-table">
    <tr><td class="label">To</td><td></td><td class="label">From</td><td></td></tr>
    <tr><td class="label">Fax</td><td></td><td class="label">Pages</td><td></td></tr>
    <tr><td class="label">Phone</td><td></td><td class="label">Date</td><td></td></tr>
    <tr><td class="label">Re</td><td></td><td class="label">CC</td><td></td></tr>
  </table>
  <div class="fax-options">
    <span><i></i>Urgent</span>
    <span><i></i>For Review</span>
    <span><i></i>Please Comment</span>
    <span><i></i>Please Reply</span>
    <span><i></i>Please Recycle</span>
  </div>
</div>

</body>
</html>
```